Custom LED sign business needs logo and web design.

We need a logo and website design for a new company based in Austin TX. What we do is laser engrave custom artwork for led edge lit signs. Our marketing will be directed to kids rooms, game rooms and business. I would like to see designs that have a neon text effect. The look should feel professional for businesses and fun for kids.

**UPDATE** This website will need a custom design page that uses Quillmark Item Composer type plugin. The users will be able to choose from pre-loaded artwork and fonts or upload there own artwork.
There will also be a ecommerce tab that will. have ready to ship signs available.
Wordpress will be the platform used.

Target Market(s)

Businesses, kids and game rooms

Neon Text effect with logo. Professional but fun.

Logo Text

Vorbrights

Number of Pages Required

5+ page

Font styles to use
Other font styles liked:
• A neon text effect type font. Example picture added

Colors

Designer to choose colors to be used in the design.

Requirements
Must have
• Neon Text effects with a professional tech look. Incorporate the "create", "energize" and "amaze" as the company slogan.
• Quillmark Item Composer for customer interactive sign design.
• Ecommerce platform so that I can upload ready to ship signs.
• Refer to the Create, Energize, Amaze pics attached as company slogan. Use those fonts.
Nice to have
• I would like text to "turn on" when hovered over.
Should not have
• Scattered text locations. Unorganized layout and feel.

```html
<!DOCTYPE html>
<html lang="en">
<head>
<meta charset="utf-8">
<title>Vorbrights — Custom LED Edge Lit Signs</title>
<link rel="stylesheet" href="https://fonts.googleapis.com/css2?family=Almendra+SC&family=Black+Ops+One&family=Permanent+Marker&family=Nunito+Sans:wght@400;600;700&family=Roboto:wght@400;500&display=swap">
<style>
:root{
  --ink:#0a0506;
  --bar:#1c1114;
  --panel-a:#26171b;
  --panel-b:#2e2126;
  --teal:#2ee6c2;
  --teal-dim:#1fa88e;
  --orange:#f08a3a;
  --text:#d9d2d4;
  --muted:#8c8285;
  --white:#ffffff;
  --red-neon:#ff3b4e;
  --blue-neon:#27d3ff;
  --green-neon:#3dff57;
}
*{margin:0;padding:0;box-sizing:border-box}
html,body{width:1200px;height:2683px;overflow:hidden;background:var(--ink)}
body{position:relative;font-family:"Roboto",Arial,sans-serif;color:var(--text)}
.abs{position:absolute}
a{color:inherit;text-decoration:none}

.topbar{left:0;top:0;width:1200px;height:36px;background:var(--bar);font-size:9px;letter-spacing:.5px;color:var(--muted)}
.topbar .account{left:250px;top:12px}
.topbar .checkout{left:332px;top:12px}
.topbar .cart{left:855px;top:11px;color:var(--text);display:flex;align-items:center;gap:6px}
.mainnav{left:0;top:36px;width:1200px;height:48px;background:var(--panel-a);border-bottom:1px solid #3a2a2f}
.navlink{top:18px;font-size:9px;letter-spacing:.6px;color:var(--text)}
.navlink.active{color:var(--teal)}
.navlink.active::after{content:"";position:absolute;left:-14px;right:-14px;top:29px;height:2px;background:var(--teal)}
.brand{left:552px;top:20px;width:96px;height:96px;border-radius:50%;background:#120a0c;display:flex;align-items:center;justify-content:center;font-family:"Nunito Sans",sans-serif;font-weight:700;font-size:15px;color:var(--white)}

.hero{left:0;top:84px;width:1200px;height:377px;background:radial-gradient(ellipse at 45% 45%,#3a1c1c 0%,#24100f 55%,#140909 100%)}
.slogan{font-size:48px;line-height:1}
.slogan.create{left:250px;top:154px;font-family:"Almendra SC",serif;color:#ff6f7c;text-shadow:0 0 6px var(--red-neon),0 0 18px var(--red-neon),0 0 36px #c3162a}
.slogan.energize{left:442px;top:226px;font-family:"Black Ops One",sans-serif;font-size:50px;color:#8af0ff;text-shadow:0 0 6px var(--blue-neon),0 0 18px var(--blue-neon),0 0 40px #0a8fd6}
.slogan.amaze{left:700px;top:316px;font-family:"Permanent Marker",cursive;font-size:50px;color:#9dff9e;transform:rotate(-3deg);text-shadow:0 0 6px var(--green-neon),0 0 18px var(--green-neon),0 0 36px #13a82a}

.cta{top:461px;width:600px;height:183px}
.cta.shop{left:0;background:var(--panel-a)}
.cta.custom{left:600px;background:var(--panel-b)}
.cta h2{position:absolute;top:30px;display:flex;align-items:center;gap:8px;font-family:"Nunito Sans",sans-serif;font-weight:400;font-size:19px;color:var(--orange);text-shadow:0 0 10px rgba(240,138,58,.55)}
.cta p{position:absolute;top:74px;width:280px;font-size:10px;line-height:16px;color:var(--text)}
.btn{position:absolute;height:31px;border:1px solid var(--teal-dim);color:var(--teal);font-size:8px;letter-spacing:.8px;display:flex;align-items:center;justify-content:center;font-weight:500}
.cta.shop h2,.cta.shop p{left:250px}
.cta.custom h2,.cta.custom p{left:70px}
.cta.shop .btn{left:250px;top:120px;width:101px}
.cta.custom .btn{left:70px;top:120px;width:101px}

.section-title{left:0;width:1200px;text-align:center;font-family:"Nunito Sans",sans-serif;font-weight:400;font-size:24px;color:var(--teal);text-shadow:0 0 8px rgba(46,230,194,.7),0 0 22px rgba(46,230,194,.4)}
.featured-title{top:690px}
.product{width:222px}
.product .thumb{width:222px;height:221px}
.product .meta{display:flex;justify-content:space-between;margin-top:12px;font-size:9px;color:var(--text)}
.product .price{color:var(--white);font-weight:500;font-size:10px}
.view-all{left:552px;top:1320px;width:95px}

.about{left:0;top:1400px;width:1200px;height:329px;background:linear-gradient(180deg,#1f0f10,#2b1514 50%,#1a0c0d)}
.about h2{position:absolute;left:250px;top:50px;font-family:"Nunito Sans",sans-serif;font-weight:400;font-size:24px;color:var(--orange);text-shadow:0 0 10px rgba(240,138,58,.55)}
.about p{position:absolute;left:250px;top:104px;width:340px;font-size:10px;line-height:15px}
.about .btn{left:250px;top:204px;width:95px}
.video{left:610px;top:52px;width:340px;height:229px;background:linear-gradient(135deg,#6f6a6d,#a9a2a3 45%,#5c4e56)}

.blog-title{top:1770px}
.post{width:340px}
.post .thumb{height:127px}
.post h3{margin-top:16px;font-family:"Roboto",sans-serif;font-weight:500;font-size:16px;line-height:19px;color:var(--white)}
.post .date{margin-top:10px;font-size:8px;color:var(--muted);display:flex;gap:14px}
.post p{margin-top:14px;font-size:9.5px;line-height:15px}
.post .btn{right:0;top:287px;width:93px}

.newsletter{left:0;top:2235px;width:1200px;height:155px;background:var(--panel-a)}
.newsletter h2{position:absolute;left:250px;top:42px;display:flex;align-items:center;gap:8px;font-family:"Nunito Sans",sans-serif;font-weight:400;font-size:19px;color:var(--orange);text-shadow:0 0 10px rgba(240,138,58,.55)}
.newsletter p{position:absolute;left:250px;top:84px;width:330px;font-size:10px;line-height:15px}
.signup{left:610px;top:62px;width:340px;height:31px;border:1px solid var(--teal-dim);display:flex}
.signup .field{flex:1;font-size:9px;color:var(--muted);padding:10px 10px}
.signup .go{width:94px;border-left:1px solid var(--teal-dim);color:var(--teal);font-size:8px;letter-spacing:.8px;display:flex;align-items:center;justify-content:center}

.footer{left:0;top:2390px;width:1200px;height:247px;background:#050203}
.footer .mark{left:250px;top:80px;font-family:"Nunito Sans",sans-serif;font-weight:700;font-size:16px;color:#2c2326}
.social{top:168px;width:10px;height:10px;border-radius:50%;background:var(--white)}
.fcol{top:76px}
.fcol h4{font-family:"Nunito Sans",sans-serif;font-weight:400;font-size:14px;color:var(--teal);text-shadow:0 0 8px rgba(46,230,194,.5);margin-bottom:18px}
.fcol li{list-style:none;font-size:9.5px;color:var(--text);height:30px}
.copyright{left:0;top:2637px;width:1200px;height:46px;background:var(--bar);text-align:center;font-size:9.5px;color:var(--text);padding-top:17px}
</style>
</head>
<body>

<div class="abs topbar">
  <a class="abs account" href="#">MY ACCOUNT</a>
  <a class="abs checkout" href="#">CHECKOUT</a>
  <div class="abs cart">
    <svg width="11" height="10" viewBox="0 0 11 10"><path d="M0 1h2l1.5 5h6L11 2.5H3" fill="none" stroke="#d9d2d4" stroke-width="1.2"/><circle cx="4" cy="8.5" r="1" fill="#d9d2d4"/><circle cx="8.5" cy="8.5" r="1" fill="#d9d2d4"/></svg>
    <span>3 ITEMS - $540.99</span>
  </div>
</div>

<nav class="abs mainnav">
  <a class="abs navlink active" style="left:352px" href="#">HOME</a>
  <a class="abs navlink" style="left:408px" href="#">SHOP</a>
  <a class="abs navlink" style="left:464px" href="#">CUSTOMISE</a>
  <a class="abs navlink" style="left:685px" href="#">BLOG</a>
  <a class="abs navlink" style="left:737px" href="#">ABOUT US</a>
  <a class="abs navlink" style="left:812px" href="#">CONTACT US</a>
</nav>
<div class="abs brand">Vorbrights</div>

<section class="abs hero" role="img" aria-label="Dark red brick wall lit by neon glow"></section>
<div class="abs slogan create">CREATE</div>
<div class="abs slogan energize">ENERGIZE</div>
<div class="abs slogan amaze">AMAZE</div>

<section class="abs cta shop">
  <h2><svg width="20" height="18" viewBox="0 0 20 18"><path d="M1 2h3l2.5 9h10L19 5H5" fill="none" stroke="#f08a3a" stroke-width="1.6"/><circle cx="8" cy="15" r="1.6" fill="#f08a3a"/><circle cx="15" cy="15" r="1.6" fill="#f08a3a"/></svg>GO SHOPPING</h2>
  <p>Choose from our wide range of laser engraved led edge lit signs.</p>
  <a class="btn" href="#">GO TO SHOP</a>
</section>
<section class="abs cta custom">
  <h2><svg width="18" height="18" viewBox="0 0 18 18"><path d="M2 2l14 14M16 2L2 16M2 2l3 0M2 2l0 3M16 2l-3 0M16 2l0 3" fill="none" stroke="#f08a3a" stroke-width="1.6"/></svg>CUSTOMIZE YOUR OWN</h2>
  <p>Customise and design your sign and we will engrave and deliver it to you.</p>
  <a class="btn" href="#">GO TO EDITOR</a>
</section>

<h2 class="abs section-title featured-title">FEATURED PRODUCTS</h2>

<div class="abs product" style="left:250px;top:760px"><div class="thumb" role="img" aria-label="Red lit sign with a flaming billiard ball" style="background:radial-gradient(circle at 40% 50%,#ff5a5a,#b0151c 50%,#2a0406)"></div><div class="meta"><span>Product Name</span><span class="price">$199.99</span></div></div>
<div class="abs product" style="left:490px;top:760px"><div class="thumb" role="img" aria-label="Blue lit barber shop sign" style="background:radial-gradient(circle at 50% 45%,#3f6dff,#1431b8 50%,#050a30)"></div><div class="meta"><span>Product Name</span><span class="price">$199.99</span></div></div>
<div class="abs product" style="left:730px;top:760px"><div class="thumb" role="img" aria-label="Gold lit happy birthday sign" style="background:radial-gradient(circle at 50% 50%,#f6b52a,#8f5a08 55%,#1e1203)"></div><div class="meta"><span>Product name</span><span class="price">$199.99</span></div></div>
<div class="abs product" style="left:250px;top:1033px"><div class="thumb" role="img" aria-label="Green lit graffiti word sign" style="background:radial-gradient(circle at 50% 45%,#4dff62,#13a01f 50%,#052a08)"></div><div class="meta"><span>Product name</span><span class="price">$199.99</span></div></div>
<div class="abs product" style="left:490px;top:1033px"><div class="thumb" role="img" aria-label="Magenta lit name sign" style="background:radial-gradient(circle at 50% 50%,#ff5cf2,#b11bbf 55%,#30053a)"></div><div class="meta"><span>Product name</span><span class="price">$199.99</span></div></div>
<div class="abs product" style="left:730px;top:1033px"><div class="thumb" role="img" aria-label="Red lit word sign on a wall" style="background:linear-gradient(180deg,#1a0809,#d32030 45%,#7a0d14 70%,#1a0809)"></div><div class="meta"><span>Product name</span><span class="price">$199.99</span></div></div>

<a class="btn view-all" href="#">VIEW ALL</a>

<section class="abs about" role="region" aria-label="About us">
  <h2>ABOUT US</h2>
  <p>Lorem ipsum dolor sit amet, vis id sumo omnis periculis, vim ad eius exerci, epicuri expetendis et eum. Eum laboramus abhorreant eu, velit nostro legendos in per, an mucius virtute principes sed. Volumus dignissim id has, vix delectus reprimique eu. Impetus veritus definiebas his an, vis modo soleat consequuntur ad.</p>
  <a class="btn" href="#">LEARN MORE</a>
  <div class="abs video" role="img" aria-label="Video still of a laser engraver cutting an acrylic panel"></div>
</section>

<h2 class="abs section-title blog-title">FROM THE BLOG</h2>

<article class="abs post" style="left:250px;top:1843px">
  <div class="thumb" role="img" aria-label="Gold outline lettering sign glowing on a dark shelf" style="background:linear-gradient(90deg,#2a2418,#5b4a25 50%,#1e1a12)"></div>
  <h3>Lorem ipsum dolor sit amet, vis id sumomnis periculis vim ad</h3>
  <div class="date"><span>6th Aug, 2018</span><span>admin</span></div>
  <p>Lorem ipsum dolor sit amet, vis id sumo omnis periculis, vim ad eius exerci, epicuri expetendis et eum. Eum laboramus abhorreant eu, velit nostro legendos in per, an mucius virtute principes sed...</p>
  <a class="btn" href="#">READ MORE</a>
</article>
<article class="abs post" style="left:610px;top:1843px">
  <div class="thumb" role="img" aria-label="Blue and pink lit acrylic lettering sign" style="background:linear-gradient(90deg,#5a3aa8,#2c7be0 50%,#9a5ac8)"></div>
  <h3>An aeterno labitur nonumes vix, justo epicurei similique ad duo</h3>
  <div class="date"><span>6th Aug, 2018</span><span>admin</span></div>
  <p>An aeterno labitur nonumes vix, justo epicurei similique ad duo. An vero quodsi pro, duis viderer te vix, sit ne soleat necessitatibus. Eam autem sanctus at. Ius ei tota maiorum...</p>
  <a class="btn" href="#">READ MORE</a>
</article>

<section class="abs newsletter">
  <h2><svg width="18" height="16" viewBox="0 0 18 16"><rect x="1" y="4" width="16" height="11" fill="none" stroke="#f08a3a" stroke-width="1.5"/><path d="M1 4l8 6 8-6M1 4l8-3 8 3" fill="none" stroke="#f08a3a" stroke-width="1.5"/></svg>NEWSLETTER SUBSCRIPTION</h2>
  <p>Recieve our latest offers, invites and discounts directly in your mail. We don't spam, promise!</p>
  <div class="abs signup"><span class="field">Your Email</span><span class="go">SIGN UP</span></div>
</section>

<footer class="abs footer">
  <div class="abs mark">Vorbrights</div>
  <span class="abs social" style="left:250px" aria-label="Social link"></span>
  <span class="abs social" style="left:281px" aria-label="Social link"></span>
  <span class="abs social" style="left:312px" aria-label="Social link"></span>
  <div class="abs fcol" style="left:429px"><h4>ABOUT US</h4><ul><li>About Us</li><li>Blog</li><li>Testimonials</li></ul></div>
  <div class="abs fcol" style="left:608px"><h4>LINKS</h4><ul><li>Products</li><li>Customize</li><li>Best Sellers</li></ul></div>
  <div class="abs fcol" style="left:789px"><h4>LEGAL</h4><ul><li>Privacy Policy</li><li>Terms of Use</li><li>Site Map</li></ul></div>
</footer>
<div class="abs copyright">Copyright © 2018 Vorbrights</div>

</body>
</html>
```